New Business Card Needed

I need a new business card for Willowmere Kitchen & Bath.
Logo is attached as well a my photo. Note: Make the logo Navy Blue.
Here is the text:
Desmond Ferrick
GC/Owner
Charlotte NC
704-555-0183
desmond@willowmereKB.example
www.willowmereKB.example
Tag line on card: BEAUTY | FUNCTION | ON TIME | ON BUDGET
Trim size: 2.56" X 2.56"
This is where we aim to cut the cards.
Safe area: 2.4" X 2.4"
Make sure any important aspects of your design such as text and logos are inside of the safe area, otherwise they may be cut off.
Bleed area: 2.71 X 2.71
Make sure that your background extends to fill the bleed to avoid your Business Cards having white edges when trimmed.
On the back side. Use photo of kitchen attached.

```html
<!DOCTYPE html>
<html lang="en">
<head>
<meta charset="utf-8">
<title>Willowmere Kitchen &amp; Bath — Business Card</title>
<link href="https://fonts.googleapis.com/css2?family=Montserrat:wght@300;400;600;700&display=swap" rel="stylesheet">
<style>
  :root {
    --sheet: #ffffff;
    --burgundy: #7a0019;
    --blush: #f6b8b8;
    --text-light: #f1d3d3;
    --white: #ffffff;
    --guide-bleed: #e8262b;
    --guide-trim: #3b3bd6;
    --guide-safe: #2e8b57;
    --kitchen-cream: #efe9df;
    --kitchen-white: #f7f4ef;
    --kitchen-counter: #8a8178;
    --kitchen-wood: #c99a64;
  }
  * { margin: 0; padding: 0; box-sizing: border-box; }
  html, body { width: 1200px; height: 625px; overflow: hidden; background: var(--sheet); }
  .sheet { position: relative; width: 1200px; height: 625px; font-family: "Montserrat", Arial, sans-serif; }

  .card { position: absolute; top: 47px; width: 522px; height: 522px; overflow: hidden; }
  .card--front { left: 43px; background: var(--burgundy); }
  .card--back { left: 634px; }

  .guide { position: absolute; pointer-events: none; }
  .guide--bleed { inset: 0; border: 1px solid var(--guide-bleed); }
  .guide--trim { left: 15px; top: 15px; width: 492px; height: 493px; border: 1px solid var(--guide-trim); }
  .guide--safe { left: 30px; top: 30px; width: 462px; height: 462px; border: 1px solid var(--guide-safe); opacity: .8; }

  .brand-name {
    position: absolute; left: 50px; top: 114px;
    color: var(--blush); font-weight: 400; font-size: 22px; letter-spacing: .03em; white-space: nowrap;
  }

  .contact { position: absolute; left: 50px; top: 218px; list-style: none; color: var(--text-light); }
  .contact li { font-weight: 300; font-size: 23px; line-height: 40px; letter-spacing: .01em; white-space: nowrap; }
  .contact .contact__web { font-weight: 700; color: var(--white); }

  .photo {
    position: absolute; inset: 0;
    background: linear-gradient(180deg, var(--kitchen-cream) 0%, var(--kitchen-white) 45%, var(--kitchen-counter) 72%, var(--kitchen-wood) 100%);
  }
  .photo::after {
    content: ""; position: absolute; inset: 0;
    background: radial-gradient(ellipse at 15% 30%, rgba(180,110,60,.35), transparent 45%);
  }

  .tagline {
    position: absolute; left: 30px; right: 30px; top: 415px;
    text-align: center; color: var(--white);
    font-weight: 600; font-size: 23px; line-height: 29px; letter-spacing: .02em;
    text-shadow: 0 1px 3px rgba(0,0,0,.45);
  }
</style>
</head>
<body>
<main class="sheet">
  <section class="card card--front" aria-label="Front of card">
    <p class="brand-name">Willowmere Kitchen &amp; Bath</p>
    <ul class="contact">
      <li>Desmond Ferrick</li>
      <li>GC/Owner</li>
      <li>Charlotte NC</li>
      <li>704-555-0183</li>
      <li>desmond@willowmereKB.example</li>
      <li class="contact__web">www.willowmereKB.example</li>
    </ul>
    <div class="guide guide--bleed"></div>
    <div class="guide guide--trim"></div>
    <div class="guide guide--safe"></div>
  </section>

  <section class="card card--back" aria-label="Back of card">
    <div class="photo" role="img" aria-label="Photo of a bright white kitchen with hanging copper pots, a stone-topped island and a woven runner on a wood floor"></div>
    <p class="tagline">BEAUTY | FUNCTION | ON TIME |<br>ON BUDGET</p>
    <div class="guide guide--bleed"></div>
    <div class="guide guide--safe"></div>
  </section>
</main>
</body>
</html>
```